Safety Brochure for Industry Assocations

This is an 8.5 x 11 single sided brochure for our Occupational Health and Safety Data Analytics software. If you need to use stock images we will pay for them.

Please incorporate our logo and some of the images. No need to incorporate them all. We like the idea of the boots being at the bottom of the page but we're open to other ideas.

Please note that we intend to mail this brochure to different industries so it should be generic (i.e. not construction specific).

Target Market(s)

Safety and Industry Organisations for construction, mining, forestry and oil and gas industries.

Industry/Entity Type

Industry

Font styles to use
Sans Serif

Colors

Designer to choose colors to be used in the design.

Requirements
Must have
• We are a software company that produces safety software. Our customers are companies that engage in dangerous work and use our software to improve their worker's safety. The look and feel should convey the fact that:
• -We are Big Data
• -We are Software
• -We service industry
Nice to have
• Please see the Pixlore photo of the boots. We were hoping that the desiger would be able ti modify the image with an overlay of 0's and 1's in a kind of "matrix" fashion to indicate that we are merging traditional labour work with software.
Should not have
• No medical symbols. Note that WE ARE NOT HEALTH CARE.

```html
<!DOCTYPE html>
<html lang="en">
<head>
<meta charset="utf-8">
<title>Leverage the power of Big Data – Safety Brochure</title>
<link href="https://fonts.googleapis.com/css2?family=Arvo:wght@400;700&family=Roboto+Slab:wght@300;400&display=swap" rel="stylesheet">
<style>
  :root {
    --navy: #083a6b;
    --teal: #1a8ba9;
    --green: #3fae49;
    --ink: #0f2f55;
    --paper: #ffffff;
    --backdrop: #e9ebee;
  }
  * { box-sizing: border-box; margin: 0; padding: 0; }
  html, body { width: 1200px; height: 1000px; overflow: hidden; background: var(--backdrop); }
  .brochure {
    position: absolute; left: 229px; top: 20px;
    width: 742px; height: 960px;
    background: var(--paper);
    box-shadow: 0 6px 24px rgba(0,0,0,.18);
    overflow: hidden;
    font-family: "Roboto Slab", serif;
    color: var(--navy);
  }
  .header-band { position: absolute; left: 0; top: 0; width: 742px; height: 230px; }
  .headline { position: absolute; left: 0; top: 34px; width: 742px; text-align: center; color: var(--paper); }
  .headline .lead-in { font-family: "Roboto Slab", serif; font-weight: 300; font-size: 34px; }
  .headline .big { font-family: "Arvo", serif; font-weight: 700; font-size: 58px; line-height: 1.3; }

  .pillars { position: absolute; left: 26px; top: 232px; list-style: none; }
  .pillar { display: flex; align-items: flex-start; margin-bottom: 6px; }
  .pillar-num {
    flex: none; width: 34px; height: 34px; border-radius: 50%;
    background: var(--navy); color: var(--paper);
    font-family: "Arvo", serif; font-weight: 700; font-size: 22px;
    display: flex; align-items: center; justify-content: center; margin-right: 10px;
  }
  .pillar-title { font-size: 22px; font-weight: 400; line-height: 1.1; text-transform: uppercase; }
  .pillar-sub { font-size: 15px; font-weight: 300; line-height: 1.2; }

  .brand { position: absolute; left: 535px; top: 212px; display: flex; align-items: center; gap: 10px; }
  .brand-dot { width: 36px; height: 36px; border-radius: 50%; background: var(--green); }
  .brand-name { font-family: "Roboto Slab", serif; font-weight: 400; font-size: 19px; color: var(--ink); line-height: 1.05; }

  .steps { position: absolute; left: 40px; top: 470px; width: 230px; }
  .step { display: flex; align-items: center; gap: 14px; margin-bottom: 22px; }
  .step-label { font-family: "Arvo", serif; font-weight: 700; font-size: 19px; line-height: 1.15; color: var(--navy); }
  .step-icon { flex: none; width: 56px; height: 56px; }

  .boots {
    position: absolute; left: 70px; top: 720px; width: 230px; height: 150px;
    background: linear-gradient(160deg, #1c3a14, #0d1d0a 60%, #2f7a22);
    border-radius: 10px;
  }
  .diagram { position: absolute; left: 0; top: 0; width: 742px; height: 960px; }
  .diagram text { font-family: "Arvo", serif; font-weight: 700; fill: var(--paper); text-anchor: middle; }
  .phone { position: absolute; right: 34px; bottom: 26px; font-family: "Arvo", serif; font-weight: 700; font-size: 22px; color: #111; }
</style>
</head>
<body>
<main class="brochure">
  <svg class="header-band" viewBox="0 0 742 230" aria-hidden="true">
    <path fill="var(--navy)" d="M0 0H742V150 Q700 200 650 175 Q610 225 550 200 Q500 235 440 205 Q380 235 320 205 Q260 232 200 200 Q140 228 80 195 Q40 215 0 190Z"/>
  </svg>
  <header class="headline">
    <div class="lead-in">Leverage the power of</div>
    <div class="big">Big Data!</div>
  </header>

  <ol class="pillars">
    <li class="pillar"><span class="pillar-num">1</span><div><div class="pillar-title">Lead</div><div class="pillar-sub">The next wave of injury reduction</div></div></li>
    <li class="pillar"><span class="pillar-num">2</span><div><div class="pillar-title">Engage</div><div class="pillar-sub">With Members by Collaboration and Benchmarking</div></div></li>
    <li class="pillar"><span class="pillar-num">3</span><div><div class="pillar-title">Promote <span class="pillar-sub">Standardization</span></div></div></li>
    <li class="pillar"><span class="pillar-num">4</span><div><div class="pillar-title">Analyze</div><div class="pillar-sub">Accurate, Timely &amp; Complete Leading Indicators</div></div></li>
    <li class="pillar"><span class="pillar-num">5</span><div><div class="pillar-title">Train</div><div class="pillar-sub">Industry more Proactively</div></div></li>
  </ol>

  <div class="brand"><span class="brand-dot"></span><span class="brand-name">Veridan<br>Analytics</span></div>

  <svg class="diagram" viewBox="0 0 742 960" aria-label="Data flow from EHS data to improved safety">
    <g stroke="#556" stroke-width="1.2" fill="none">
      <line x1="560" y1="360" x2="375" y2="470"/>
      <line x1="570" y1="360" x2="520" y2="520"/>
      <line x1="585" y1="360" x2="640" y2="580"/>
      <line x1="350" y1="680" x2="405" y2="790"/>
      <line x1="490" y1="735" x2="440" y2="790"/>
      <line x1="565" y1="800" x2="470" y2="830"/>
    </g>
    <g fill="var(--navy)">
      <circle cx="530" cy="335" r="34"/><circle cx="575" cy="310" r="42"/><circle cx="625" cy="335" r="32"/>
      <rect x="505" y="330" width="140" height="40" rx="20"/>
    </g>
    <text x="575" y="330" font-size="22">EHS</text>
    <text x="575" y="356" font-size="22">DATA</text>

    <g fill="var(--teal)">
      <circle cx="375" cy="470" r="40"/><circle cx="520" cy="525" r="40"/><circle cx="640" cy="590" r="40"/>
      <circle cx="420" cy="835" r="52"/>
    </g>
    <text x="375" y="476" font-size="15">Training</text>
    <text x="520" y="521" font-size="14">Bench-</text><text x="520" y="538" font-size="14">marking</text>
    <text x="640" y="586" font-size="14">Trend</text><text x="640" y="603" font-size="14">Analysis</text>
    <text x="420" y="830" font-size="18">Improve</text><text x="420" y="852" font-size="18">Safety</text>

    <g fill="none" stroke-width="10" stroke-linejoin="miter">
      <path d="M350 515 L375 538 L400 515" stroke="var(--navy)"/><path d="M350 532 L375 555 L400 532" stroke="var(--teal)"/>
      <path d="M495 570 L520 593 L545 570" stroke="var(--navy)"/><path d="M495 587 L520 610 L545 587" stroke="var(--teal)"/>
      <path d="M615 635 L640 658 L665 635" stroke="var(--navy)"/><path d="M615 652 L640 675 L665 652" stroke="var(--teal)"/>
    </g>

    <g fill="var(--navy)">
      <rect x="290" y="575" width="130" height="40" rx="20"/>
      <rect x="280" y="640" width="140" height="40" rx="20"/>
      <rect x="445" y="625" width="120" height="40" rx="20"/>
      <rect x="410" y="695" width="160" height="40" rx="20"/>
      <rect x="580" y="700" width="135" height="40" rx="20"/>
      <rect x="565" y="770" width="160" height="40" rx="20"/>
    </g>
    <g font-size="10.5">
      <text x="355" y="592">Analyze</text><text x="355" y="606">Need of Industry</text>
      <text x="350" y="657">Deliver</text><text x="350" y="671">Proactive Training</text>
      <text x="505" y="642">Engage</text><text x="505" y="656">With Members</text>
      <text x="490" y="712">Promote Collaborative</text><text x="490" y="726">Advancement of Safety</text>
      <text x="647" y="717">Monitor</text><text x="647" y="731">Industry Trends</text>
      <text x="645" y="787">Implement</text><text x="645" y="801">Corrective Initiatives</text>
    </g>
  </svg>

  <section class="steps">
    <div class="step">
      <span class="step-label">Set up<br>Your<br>Location</span>
      <svg class="step-icon" viewBox="0 0 56 56" aria-hidden="true"><circle cx="28" cy="28" r="27" fill="#eef2f5"/><path d="M28 12a10 10 0 0 1 10 10c0 8-10 20-10 20S18 30 18 22a10 10 0 0 1 10-10z" fill="var(--green)"/><circle cx="28" cy="22" r="4" fill="#fff"/></svg>
    </div>
    <div class="step">
      <svg class="step-icon" viewBox="0 0 56 56" aria-hidden="true"><circle cx="28" cy="28" r="27" fill="#eef2f5"/><rect x="13" y="14" width="30" height="28" rx="3" fill="var(--green)"/><circle cx="28" cy="30" r="7" fill="none" stroke="#fff" stroke-width="3" stroke-dasharray="4 2"/><circle cx="28" cy="30" r="2.5" fill="#fff"/></svg>
      <span class="step-label">Upload<br>Your<br>Data</span>
    </div>
    <div class="step">
      <span class="step-label">Start<br>Using Your<br>Dashboard</span>
      <svg class="step-icon" viewBox="0 0 56 56" aria-hidden="true"><circle cx="28" cy="28" r="27" fill="#eef2f5"/><rect x="12" y="14" width="32" height="22" rx="2" fill="var(--green)"/><rect x="16" y="18" width="24" height="3" fill="#fff"/><rect x="16" y="24" width="10" height="8" fill="#fff"/><rect x="28" y="24" width="12" height="3" fill="#fff"/><rect x="24" y="38" width="8" height="4" fill="var(--green)"/><rect x="19" y="42" width="18" height="2" fill="var(--green)"/></svg>
    </div>
  </section>

  <div class="boots" role="img" aria-label="Pair of work boots overlaid with green matrix-style ones and zeros"></div>

  <div class="phone">1-800-555-0142</div>
</main>
</body>
</html>
```